Brookvale Homes Flyer

Quarter-page leave-behind flyer for a commercial cleaning company (print)

ABOUT US
Quillon Commercial Cleaning is a Texas-owned commercial cleaning company serving Austin for over 20 years. We were recently named to Brookvale Homes's Capital Partner Roster Circle, a preferred vendor program covering apartment communities across the Austin metro. Our sales team will hand this flyer to apartment community managers during property visits.

THE JOB THIS FLYER MUST DO
A busy property manager should scan it in five seconds, understand what we do, trust us and keep the card on their desk. The call to action is booking a free walkthrough of their community. Do not include any pricing.

SPECS
Size: 4.25 x 5.5 inches (quarter of a letter page), single sided, portrait. Print ready with 0.125 inch bleed, CMYK, 300 dpi minimum. Vector preferred.

REQUIRED CONTENT
Headline: The clean your residents notice.
Badge or tagline: Brookvale Homes's Approved Austin Cleaning Company.
Supporting line: Preferred Vendor Partner in BVH's Capital Partner Roster Circle. Texas-owned, serving Austin for 20+ years.
Services (icons welcome): recurring janitorial, floor strip wax and buff, carpet extraction, windows and glass, upholstery care, pressure washing, move-in and move-out cleans, damage restoration.
Trust points: licensed and insured, background-checked crews, TrudeLink compliant, invoicing through Supplier Nook and Halvex Systems.

Social proof line: Already trusted by BVH communities. Ask your peers at The Wendlow and The Fennick on Garrow.

Call to action: Book a free walkthrough of your community. Call or email 512-555-0147 or support@quillonclean-example.com

STYLE DIRECTION
Clean, crisp and premium. Whiteness and shine should feel like part of the message. We like a deep green and teal palette with one warm accent, but strong alternative directions are welcome. Custom icons over clip art.
AVOID
Stock photos of cleaners with buckets, cartoon mascots, sparkle overload, cluttered layouts, any prices or dollar amounts.
DELIVERABLES
Print-ready PDF with bleed and crop marks, plus editable source files (AI, PSD or Figma). A version with our logo placement marked, since we will supply the logo file to the winner.

```html
<!DOCTYPE html>
<html lang="en">
<head>
<meta charset="utf-8">
<title>Quillon Commercial Cleaning – Brookvale Homes Flyer</title>
<link rel="stylesheet" href="https://fonts.googleapis.com/css2?family=Figtree:ital,wght@0,400;0,500;0,600;0,700;1,500;1,700&family=Source+Serif+4:opsz,wght@8..60,700&display=swap">
<style>
  :root {
    --green: #0c4b41;
    --green-deep: #0a3f37;
    --gold: #e2a93b;
    --ink: #1f2b2a;
    --panel: #f3f5f5;
    --rule: #9fb3ae;
    --white: #ffffff;
  }
  * { margin: 0; padding: 0; box-sizing: border-box; }
  html, body { width: 914px; height: 1200px; overflow: hidden; background: var(--white); }
  .flyer {
    position: relative; width: 914px; height: 1200px; overflow: hidden;
    background: var(--white); font-family: "Figtree", sans-serif; color: var(--ink);
  }
  .lobby-photo {
    position: absolute; left: 420px; top: 0; width: 494px; height: 570px;
    background: linear-gradient(180deg, #eef2f4 0%, #dfe6ea 35%, #eef1f2 60%, #f7f8f8 100%);
    -webkit-mask-image: linear-gradient(90deg, transparent 0%, #000 35%), linear-gradient(0deg, transparent 0%, #000 30%);
    -webkit-mask-composite: source-in;
    mask-image: linear-gradient(90deg, transparent 0%, #000 35%), linear-gradient(0deg, transparent 0%, #000 30%);
    mask-composite: intersect;
  }
  .logo-slot {
    position: absolute; left: 63px; top: 54px; width: 306px; height: 138px;
    border: 1.5px solid var(--gold); border-radius: 50%;
    display: flex; align-items: center; justify-content: center;
    font-size: 34px; font-weight: 500; color: var(--green-deep);
  }
  .headline {
    position: absolute; left: 62px; top: 268px;
    font-family: "Source Serif 4", serif; font-weight: 700;
    font-size: 79px; line-height: 74px; letter-spacing: -1px; color: var(--green);
  }
  .approval { position: absolute; left: 58px; top: 430px; width: 580px; height: 125px; }
  .approval-text {
    position: absolute; left: 218px; top: 465px;
    font-size: 23px; font-weight: 600; line-height: 28px; letter-spacing: 0.4px; color: var(--white);
    white-space: nowrap;
  }
  .approval-text .accent { color: var(--gold); }
  .support-line {
    position: absolute; left: 218px; top: 541px; font-size: 16px; line-height: 24px; color: var(--ink);
  }
  .support-line em { color: var(--green); font-weight: 500; }
  .section-title {
    position: absolute; left: 64px; top: 614px; width: 776px;
    display: flex; align-items: center; gap: 14px;
    font-size: 18px; font-weight: 600; letter-spacing: 2.5px; color: var(--green);
  }
  .section-title::before, .section-title::after { content: ""; flex: 1; height: 1px; background: var(--green); }
  .services { position: absolute; left: 58px; top: 648px; display: flex; list-style: none; }
  .service {
    width: 98px; height: 112px; text-align: center;
    border-right: 1px solid #c8d2cf;
    font-size: 11px; font-weight: 600; line-height: 15px; letter-spacing: 0.3px; color: var(--green);
    white-space: nowrap;
  }
  .service--tight { font-size: 10px; letter-spacing: -0.2px; }
  .service:last-child { border-right: none; }
  .service svg { display: block; margin: 6px auto 14px; width: 56px; height: 60px; }
  .trust-panel { position: absolute; left: 0; top: 790px; width: 914px; height: 260px; background: var(--panel); }
  .panel-heading {
    position: absolute; font-size: 17.5px; font-weight: 600; letter-spacing: 2px; line-height: 23px; color: var(--green);
  }
  .trust-list { position: absolute; left: 138px; top: 846px; list-style: none; }
  .trust-item { display: flex; align-items: center; height: 46px; font-size: 12.5px; font-weight: 500; letter-spacing: 0.4px; line-height: 16px; color: var(--green); }
  .trust-item svg { width: 40px; height: 40px; margin-right: 15px; flex: none; }
  .panel-divider { position: absolute; left: 469px; top: 822px; width: 1px; height: 194px; background: #c4cdcb; }
  .skyline {
    position: absolute; left: 572px; top: 872px; width: 202px; height: 64px;
    background: linear-gradient(0deg, rgba(226,169,59,0.28), rgba(226,169,59,0.06));
    border-bottom: 2px solid var(--gold);
  }
  .peers { position: absolute; left: 570px; top: 952px; font-size: 19px; line-height: 25px; color: var(--ink); }
  .peers strong { font-style: italic; font-weight: 700; color: var(--green); }
  .cta-band { position: absolute; left: 0; top: 1050px; width: 914px; height: 150px; background: var(--green); }
  .cta-icon { position: absolute; left: 56px; top: 1069px; width: 82px; height: 82px; }
  .cta-text { position: absolute; left: 166px; top: 1083px; font-size: 22.5px; font-weight: 500; line-height: 28px; letter-spacing: 0.8px; color: var(--white); }
  .cta-text .accent { color: var(--gold); font-weight: 700; }
  .cta-divider { position: absolute; left: 536px; top: 1082px; width: 1px; height: 64px; background: var(--gold); }
  .contact { position: absolute; left: 562px; top: 1078px; list-style: none; color: var(--white); }
  .contact li { display: flex; align-items: center; height: 36px; font-size: 17px; font-weight: 500; white-space: nowrap; }
  .contact svg { width: 31px; height: 31px; margin-right: 14px; flex: none; }
</style>
</head>
<body>
<main class="flyer">
  <div class="lobby-photo" role="img" aria-label="Bright, glossy apartment lobby with glass walls, polished floor, lounge seating and a potted plant"></div>

  <div class="logo-slot">LOGO</div>

  <h1 class="headline">The clean your<br>residents notice</h1>

  <svg class="approval" viewBox="0 0 580 125" aria-hidden="true">
    <polygon points="140,23 564,23 578,62 564,100 140,100" fill="var(--green)"/>
    <polygon points="71,2 128,24 142,62 128,100 71,122 14,100 2,62 14,24" fill="var(--green)"/>
    <polygon points="71,9 122,29 134,62 122,95 71,115 20,95 9,62 20,29" fill="var(--white)"/>
  </svg>
  <p class="approval-text">BROOKVALE HOMES'S <span class="accent">APPROVED</span><br>AUSTIN CLEANING COMPANY</p>

  <p class="support-line">Preferred Vendor Partner in BVH's Capital Partner Roster Circle.<br><em>Texas-owned, serving Austin for 20+ years.</em></p>

  <h2 class="section-title">OUR SERVICES</h2>
  <ul class="services">
    <li class="service">
      <svg viewBox="0 0 56 60" fill="none" stroke="var(--ink)" stroke-width="2"><rect x="14" y="14" width="20" height="44"/><rect x="34" y="30" width="12" height="28"/><rect x="20" y="6" width="8" height="8"/><path d="M19 20h3M26 20h3M19 28h3M26 28h3M19 36h3M26 36h3M19 44h3M26 44h3M38 36h4M38 44h4M21 58v-7h6v7"/></svg>
      RECURRING<br>JANITORIAL
    </li>
    <li class="service">
      <svg viewBox="0 0 56 60" fill="none" stroke="var(--ink)" stroke-width="2"><path d="M16 4l8 30M14 4h6"/><rect x="18" y="34" width="22" height="14" rx="2"/><rect x="14" y="48" width="32" height="6" rx="2"/><circle cx="14" cy="54" r="4"/></svg>
      FLOOR STRIP<br>WAX &amp; BUFF
    </li>
    <li class="service">
      <svg viewBox="0 0 56 60" fill="none" stroke="var(--ink)" stroke-width="2"><path d="M44 4L30 34M30 34l-10 4-8 14h28l2-12z"/><path d="M16 52l6-10M24 52l4-8"/></svg>
      CARPET<br>EXTRACTION
    </li>
    <li class="service">
      <svg viewBox="0 0 56 60" fill="none" stroke="var(--ink)" stroke-width="2"><rect x="6" y="8" width="40" height="44"/><path d="M26 8v44M6 30h40M12 24l6-6M30 44l6-6M48 14v6M45 17h6"/></svg>
      WINDOWS<br>&amp; GLASS
    </li>
    <li class="service">
      <svg viewBox="0 0 56 60" fill="none" stroke="var(--ink)" stroke-width="2"><path d="M12 30V14a6 6 0 016-6h20a6 6 0 016 6v16"/><rect x="4" y="28" width="10" height="18" rx="4"/><rect x="42" y="28" width="10" height="18" rx="4"/><path d="M14 36h28v10H14M10 46v6M46 46v6"/><circle cx="22" cy="18" r="1"/><circle cx="34" cy="18" r="1"/></svg>
      UPHOLSTERY<br>CARE
    </li>
    <li class="service">
      <svg viewBox="0 0 56 60" fill="none" stroke="var(--ink)" stroke-width="2"><path d="M8 52c0-18 2-40 14-44 8-2 14 12 26 36"/><rect x="4" y="40" width="8" height="14" rx="2"/><path d="M46 50l2 4M50 48l4 2M44 52l0 5"/></svg>
      PRESSURE<br>WASHING
    </li>
    <li class="service service--tight">
      <svg viewBox="0 0 56 60" fill="none" stroke="var(--ink)" stroke-width="2"><rect x="12" y="4" width="32" height="52"/><rect x="16" y="8" width="24" height="48"/><circle cx="35" cy="32" r="1.5"/></svg>
      MOVE-IN &amp;<br>MOVE-OUT CLEANS
    </li>
    <li class="service">
      <svg viewBox="0 0 56 60" fill="none" stroke="var(--ink)" stroke-width="2"><path d="M28 6C22 18 12 28 12 38a16 16 0 0032 0C44 28 34 18 28 6z"/><path d="M20 40a8 8 0 006 8"/></svg>
      DAMAGE<br>RESTORATION
    </li>
  </ul>

  <section class="trust-panel" aria-label="Why managers trust us"></section>
  <h2 class="panel-heading" style="left:138px; top:813px;">YOU CAN COUNT ON US</h2>
  <ul class="trust-list">
    <li class="trust-item">
      <svg viewBox="0 0 40 40" fill="none" stroke="var(--green)" stroke-width="1.8"><circle cx="20" cy="20" r="18.5"/><path d="M20 10l8 3v6c0 6-4 9-8 11-4-2-8-5-8-11v-6z" fill="var(--green)"/><path d="M16 20l3 3 5-6" stroke="var(--white)"/></svg>
      LICENSED &amp; INSURED
    </li>
    <li class="trust-item">
      <svg viewBox="0 0 40 40" fill="none" stroke="var(--green)" stroke-width="1.8"><circle cx="20" cy="20" r="18.5"/><circle cx="20" cy="15" r="3.5" fill="var(--green)"/><circle cx="13" cy="18" r="2.5" fill="var(--green)"/><circle cx="27" cy="18" r="2.5" fill="var(--green)"/><path d="M13 28a7 7 0 0114 0zM8 28a5 5 0 018-4M32 28a5 5 0 00-8-4" fill="var(--green)"/></svg>
      BACKGROUND-CHECKED CREWS
    </li>
    <li class="trust-item">
      <svg viewBox="0 0 40 40" fill="none" stroke="var(--green)" stroke-width="1.8"><circle cx="20" cy="20" r="18.5"/><circle cx="20" cy="20" r="10" fill="var(--green)"/><path d="M15.5 20l3 3 6-6" stroke="var(--white)" stroke-width="2"/></svg>
      TRUDELINK COMPLIANT
    </li>
    <li class="trust-item">
      <svg viewBox="0 0 40 40" fill="none" stroke="var(--green)" stroke-width="1.8"><circle cx="20" cy="20" r="18.5"/><path d="M13 10h10l4 4v16H13z"/><path d="M16 17h8M16 21h8M16 25h5"/></svg>
      INVOICING THROUGH<br>SUPPLIER NOOK &amp; HALVEX SYSTEMS
    </li>
  </ul>

  <div class="panel-divider"></div>
  <h2 class="panel-heading" style="left:570px; top:813px;">ALREADY TRUSTED BY<br>BVH COMMUNITIES.</h2>
  <div class="skyline" role="img" aria-label="Line illustration of apartment towers with trees"></div>
  <p class="peers">Ask your peers at<br><strong>The Wendlow</strong> and<br><strong>The Fennick on Garrow.</strong></p>

  <section class="cta-band" aria-label="Book a walkthrough"></section>
  <svg class="cta-icon" viewBox="0 0 82 82" fill="none" stroke="var(--gold)" stroke-width="2.5"><circle cx="41" cy="41" r="39"/><rect x="23" y="25" width="36" height="32" rx="3"/><path d="M23 34h36M31 21v8M51 21v8M29 40h5M38 40h5M47 40h5M29 48h5M38 48h5"/><circle cx="52" cy="51" r="6" fill="var(--green)"/><path d="M52 48v3h2"/></svg>
  <p class="cta-text">BOOK A <span class="accent">FREE</span> WALKTHROUGH<br>OF YOUR COMMUNITY.</p>
  <div class="cta-divider"></div>
  <ul class="contact">
    <li>
      <svg viewBox="0 0 31 31"><circle cx="15.5" cy="15.5" r="15.5" fill="var(--gold)"/><path d="M11 8l3 4-2 2c1 2 3 4 5 5l2-2 4 3-2 3c-6 0-12-6-12-12z" fill="var(--green)"/></svg>
      512-555-0147
    </li>
    <li>
      <svg viewBox="0 0 31 31"><circle cx="15.5" cy="15.5" r="15.5" fill="var(--gold)"/><rect x="8" y="10" width="15" height="11" rx="1.5" fill="var(--green)"/><path d="M8.5 11l7 5.5 7-5.5" fill="none" stroke="var(--gold)" stroke-width="1.5"/></svg>
      support@quillonclean-example.com
    </li>
  </ul>
</main>
</body>
</html>
```